Graphics Design of Physics Book

Hi
Size : 8" x 11.25"
We are education book Publication Company and would like to have book cover for "Physics" it has 4 volumes. All 4 having the same color scheme and design except the volume no.
Blue is my personal favorite but u can use any color. Want to have a band at the bottom of the cover to place our Logo “VORLIN Education” a PDF of the same is attached, or you can place logo anywhere according to ur design.
I need “Physics” as title of the book to be visible prominently.
And volume and volume no. should also be Visible and eye catching I prefer a Graphic to enhance the Volume No.
A background pattern can also be a option (it should be vector form so that color can be change later)
Please do not offer any cut and paste design I need very professional presentation.
Volume and Number can be in metallic 3D (CMYK) effect.
only Professional presentation will get feedback.
I have provided a sample artwork for reference do not follow it but can be a reference what I needed !

Target Market(s)

Students Class 9th to 12th

Industry/Entity Type

Education

Font styles to use
Serif

Colors
3176b5
0555a3
85abd2
cadf82
abd036
9bcb3c

Requirements
Must have
• Eye catching.
• “Physics” as title of the book to be visible prominently.
• volume and volume no. should also be Visible and eye catching
• I prefer a Graphic to enhance the Volume No.
• Icons for
• 1. Questions and answers
• 2. Theory Notes
• 3. Tips & Tricks
• 4. Previous Year's Reference Questions
• 5. Covers Complete Syllabus
Nice to have
• decent seamless background or metallic 3d effect (not to be print in special Ink) design should only be in CMYK.
Should not have
• Physics related Pictures or Icons (Specially E=mc2) or any scientist photograph or I Need pure graphic design

```html
<!DOCTYPE html>
<html lang="en">
<head>
<meta charset="utf-8">
<title>Physics Volume 1 – Book Cover</title>
<link rel="stylesheet" href="https://fonts.googleapis.com/css2?family=Open+Sans:ital,wght@0,400;0,700;0,800;1,400;1,600&display=swap">
<style>
  :root {
    --page-bg: #eceef1;
    --paper: #ffffff;
    --blue-deep: #0555a3;
    --blue-mid: #3176b5;
    --blue-light: #85abd2;
    --blue-glow: #5fa3dc;
    --ink-blue: #0d4fa0;
  }
  * { margin: 0; padding: 0; box-sizing: border-box; }
  html, body {
    width: 1200px; height: 976px; overflow: hidden;
    background: var(--page-bg);
    font-family: "Open Sans", Arial, sans-serif;
  }
  .spread {
    position: relative; width: 1200px; height: 976px;
    display: flex; justify-content: center; align-items: center; gap: 40px;
  }
  .cover {
    position: relative; width: 555px; height: 780px;
    background: var(--paper);
    box-shadow: 0 6px 24px rgba(0,0,0,.18);
    overflow: hidden;
  }
  .cover-art { position: absolute; inset: 0; width: 100%; height: 100%; }

  .publisher {
    position: absolute; left: 0; top: 430px;
    background: var(--blue-deep);
    border: 2px solid #fff; border-left: none;
    padding: 6px 14px 6px 18px;
    color: #fff; font-weight: 700; font-size: 20px; letter-spacing: .5px;
  }

  .title {
    position: absolute; right: 34px; top: 36px;
    font-weight: 800; font-size: 64px; letter-spacing: 4px;
    color: #fff;
    text-shadow: 2px 3px 4px rgba(0,20,70,.45);
  }

  .features {
    position: absolute; left: 60px; top: 300px;
    list-style: none;
    color: var(--ink-blue); font-style: italic; font-weight: 600; font-size: 19px;
  }
  .features li { display: flex; align-items: center; gap: 10px; margin-bottom: 8px; }
  .features svg { width: 16px; height: 16px; flex: none; }

  .volume { position: absolute; left: 0; bottom: 30px; width: 555px; height: 150px; }
</style>
</head>
<body>
<main class="spread">

  <section class="cover cover--back" aria-label="Back cover">
    <svg class="cover-art" viewBox="0 0 555 780" preserveAspectRatio="none">
      <defs>
        <radialGradient id="back-band" cx="0.35" cy="0.55" r="0.7">
          <stop offset="0" stop-color="var(--blue-glow)"/>
          <stop offset="0.6" stop-color="var(--blue-mid)"/>
          <stop offset="1" stop-color="var(--blue-deep)"/>
        </radialGradient>
      </defs>
      <path d="M0 250 C 120 250 220 380 330 520 C 400 610 470 680 555 700 L555 780 L0 780 Z" fill="url(#back-band)"/>
      <path d="M0 232 C 130 232 230 365 345 510 C 415 600 480 665 555 682" fill="none" stroke="var(--blue-deep)" stroke-width="5"/>
    </svg>
    <div class="publisher">VORLIN Education</div>
  </section>

  <section class="cover cover--front" aria-label="Front cover">
    <svg class="cover-art" viewBox="0 0 555 780" preserveAspectRatio="none">
      <defs>
        <radialGradient id="top-band" cx="0.6" cy="0.4" r="0.8">
          <stop offset="0" stop-color="var(--blue-glow)"/>
          <stop offset="0.6" stop-color="var(--blue-mid)"/>
          <stop offset="1" stop-color="var(--blue-deep)"/>
        </radialGradient>
        <radialGradient id="bottom-band" cx="0.5" cy="0.6" r="0.8">
          <stop offset="0" stop-color="var(--blue-glow)"/>
          <stop offset="0.55" stop-color="var(--blue-mid)"/>
          <stop offset="1" stop-color="var(--blue-deep)"/>
        </radialGradient>
      </defs>
      <path d="M0 0 L555 0 L555 240 C 480 240 440 200 380 165 C 300 120 200 120 0 120 Z" fill="url(#top-band)"/>
      <path d="M0 136 C 200 136 300 136 380 182 C 440 218 480 256 555 256" fill="none" stroke="var(--blue-deep)" stroke-width="5"/>
      <path d="M0 560 C 150 545 260 560 360 600 C 440 632 500 650 555 650 L555 780 L0 780 Z" fill="url(#bottom-band)"/>
      <path d="M0 544 C 150 528 265 544 365 584 C 445 616 500 634 555 634" fill="none" stroke="var(--blue-deep)" stroke-width="5"/>
    </svg>

    <h1 class="title">PHYSICS</h1>

    <ul class="features">
      <li><svg viewBox="0 0 16 16"><path d="M2 9 L6 13 L14 3" fill="none" stroke="var(--blue-deep)" stroke-width="2.4"/></svg>Questions and answers</li>
      <li><svg viewBox="0 0 16 16"><path d="M2 9 L6 13 L14 3" fill="none" stroke="var(--blue-deep)" stroke-width="2.4"/></svg>Theory Notes</li>
      <li><svg viewBox="0 0 16 16"><path d="M2 9 L6 13 L14 3" fill="none" stroke="var(--blue-deep)" stroke-width="2.4"/></svg>Tips &amp; Tricks</li>
      <li><svg viewBox="0 0 16 16"><path d="M2 9 L6 13 L14 3" fill="none" stroke="var(--blue-deep)" stroke-width="2.4"/></svg>Previous Year's Reference Questions</li>
      <li><svg viewBox="0 0 16 16"><path d="M2 9 L6 13 L14 3" fill="none" stroke="var(--blue-deep)" stroke-width="2.4"/></svg>Covers Complete Syllabus</li>
    </ul>

    <svg class="volume" viewBox="0 0 555 150">
      <defs>
        <linearGradient id="metal" x1="0" y1="0" x2="0" y2="1">
          <stop offset="0" stop-color="#ffffff"/>
          <stop offset="0.45" stop-color="#c9ced6"/>
          <stop offset="0.5" stop-color="#7d8591"/>
          <stop offset="0.75" stop-color="#dfe3e8"/>
          <stop offset="1" stop-color="#8f97a3"/>
        </linearGradient>
      </defs>
      <text x="281" y="112" text-anchor="middle" font-family="Open Sans, Arial, sans-serif" font-weight="800" font-size="86" fill="#2b3440" opacity=".55">VOLUME-1</text>
      <text x="277" y="107" text-anchor="middle" font-family="Open Sans, Arial, sans-serif" font-weight="800" font-size="86" fill="url(#metal)" stroke="#5b6470" stroke-width="1.5">VOLUME-1</text>
    </svg>
  </section>

</main>
</body>
</html>
```